SILVER COVENANT

I need a poster design which is writing the BRIGHTWATER SCROLL which I have it
written in my book.The content is spiritual.The poster could be rolled up like a papyrus or a canvas. and could be a wall hanging with tessels and a string to hang. The writing needs to bold and in artistic calligraphy.The background could be starry sky with a light inscription in white GOD IS ONE.The border should be exquisite design in gold. The bottom of the design-border should have seven burgundy red petals.The top could be a dome with an arc of small religious symbols.
The symbols are on the cover of my book

```html
<!DOCTYPE html>
<html lang="en">
<head>
<meta charset="utf-8">
<title>Brightwater Scroll – God Is One</title>
<link rel="stylesheet" href="https://fonts.googleapis.com/css2?family=Comfortaa:wght@500;700&family=Lobster&family=Arimo:wght@400&display=swap">
<style>
  :root {
    --gold-light: #fbe7a1;
    --gold: #e7b646;
    --gold-deep: #a8731c;
    --gold-dark: #7a4d10;
    --title-gold: #f7c21c;
    --night: #1a0f4a;
    --violet: #4b1f8a;
    --magenta: #9a3d9c;
    --sky-blue: #5fa0e6;
    --petal: #8a1538;
    --dome: #d9b98d;
    --ink: #ffffff;
  }
  * { margin: 0; padding: 0; box-sizing: border-box; }
  html, body { width: 900px; height: 1200px; overflow: hidden; background: #ffffff; }
  .canvas { position: relative; width: 900px; height: 1200px; }

  .frame {
    position: absolute; left: 16px; top: 18px; width: 868px; height: 1164px;
    background:
      linear-gradient(90deg, var(--gold-dark), var(--gold) 8%, var(--gold-light) 20%, var(--gold) 35%, var(--gold-deep) 50%, var(--gold) 65%, var(--gold-light) 80%, var(--gold) 92%, var(--gold-dark));
    box-shadow: inset 0 0 0 3px var(--gold-dark), 0 2px 6px rgba(0,0,0,.35);
  }
  .frame-moulding {
    position: absolute; left: 22px; top: 22px; right: 22px; bottom: 22px;
    border: 10px solid var(--gold);
    box-shadow: inset 0 0 0 2px var(--gold-dark), inset 0 0 0 7px var(--gold-light), inset 0 0 0 12px var(--gold-deep), 0 0 0 2px var(--gold-dark);
    background: linear-gradient(180deg, var(--gold-light), var(--gold) 50%, var(--gold-deep));
  }

  .poster {
    position: absolute; left: 86px; top: 86px; width: 722px; height: 1026px; overflow: hidden;
    background:
      radial-gradient(circle at 82% 14%, rgba(255,255,255,.95) 0, rgba(240,170,230,.6) 4%, rgba(180,80,170,.35) 14%, transparent 30%),
      radial-gradient(ellipse 22% 70% at 33% 30%, rgba(150,210,255,.55), transparent 70%),
      radial-gradient(ellipse at 18% 20%, rgba(60,120,210,.7), transparent 50%),
      radial-gradient(ellipse at 80% 60%, rgba(154,61,156,.55), transparent 55%),
      linear-gradient(160deg, var(--night) 0%, var(--violet) 45%, var(--magenta) 70%, var(--night) 100%);
  }
  .light-beam { position: absolute; inset: 0; }
  .flare {
    position: absolute; left: 580px; top: 820px; width: 60px; height: 60px; border-radius: 50%;
    background: radial-gradient(circle, #ffffff 0, rgba(255,220,240,.8) 20%, rgba(200,60,110,.3) 55%, transparent 70%);
  }

  .dome {
    position: absolute; left: 244px; top: 6px; width: 262px; height: 214px;
    border-radius: 131px 131px 6px 6px;
    background: radial-gradient(ellipse at 50% 35%, #ead2ad, var(--dome) 60%, #b9966a);
  }

  .title {
    position: absolute; left: 0; top: 230px; width: 722px; text-align: center;
    font-family: "Comfortaa", sans-serif; font-weight: 700; font-size: 46px;
    color: var(--title-gold); letter-spacing: 1px; white-space: nowrap;
  }
  .title .glyph { font-family: "Arimo", sans-serif; font-size: 50px; margin: 0 22px; }

  .verse {
    position: absolute; left: 0; top: 310px; width: 722px; text-align: center; color: var(--ink);
    font-family: "Arimo", sans-serif; font-size: 13.5px; line-height: 16.2px;
  }
  .verse-heading-main {
    font-family: "Lobster", cursive; font-size: 44px; line-height: 48px; margin-bottom: 2px;
    font-style: italic; margin-left: -76px;
  }
  .stanza { margin-bottom: 8px; margin-left: -76px; }
  .stanza h2 {
    font-family: "Lobster", cursive; font-weight: 400; font-size: 15px; line-height: 17px;
  }

  .petals {
    position: absolute; left: 0; bottom: 0; width: 722px; height: 80px;
    background: linear-gradient(180deg, rgba(138,21,56,0) 0%, rgba(138,21,56,.55) 55%, rgba(138,21,56,.7) 100%);
  }
  .book-line {
    position: absolute; left: 0; top: 964px; width: 722px; text-align: center; margin-left: -76px;
    font-family: "Lobster", cursive; font-size: 20px; color: var(--ink);
  }
</style>
</head>
<body>
<div class="canvas">
  <div class="frame"><div class="frame-moulding"></div></div>

  <div class="poster">
    <svg class="light-beam" width="722" height="1026" viewBox="0 0 722 1026" aria-hidden="true">
      <defs>
        <linearGradient id="beam" x1="0" y1="0" x2="0" y2="1">
          <stop offset="0" stop-color="#ffffff" stop-opacity=".7"/>
          <stop offset="1" stop-color="#bfe0ff" stop-opacity="0"/>
        </linearGradient>
      </defs>
      <path d="M330 0 L400 0 L300 1026 L60 1026 Z" fill="url(#beam)" opacity=".35"/>
      <line x1="0" y1="146" x2="722" y2="146" stroke="#ffffff" stroke-opacity=".25"/>
      <line x1="0" y1="825" x2="722" y2="825" stroke="#ffffff" stroke-opacity=".2"/>
      <line x1="470" y1="0" x2="722" y2="340" stroke="#ffffff" stroke-opacity=".25"/>
    </svg>
    <div class="flare"></div>

    <div class="dome" role="img" aria-label="Dome bearing an arc of small religious symbols"></div>

    <h1 class="title"><span class="glyph">α</span>Brightwater Scroll<span class="glyph">Ω</span></h1>

    <div class="verse">
      <p class="verse-heading-main">GOD IS ONE</p>
      <section class="stanza">
        <h2>God is Omnioneness</h2>
        <p>God is one!<br>Ye shall not divide God,<br>One for all,<br>One in all,<br>One we seek.</p>
      </section>
      <section class="stanza">
        <h2>God is Omnipresent</h2>
        <p>All present, unlimited,<br>All pervasive in the whole cosmos,<br>In you and the smallest god particle.</p>
      </section>
      <section class="stanza">
        <h2>God is Omnipotent</h2>
        <p>The all-powerful supreme Being,<br>Manifesting in all the Universes,<br>There is only one power!</p>
      </section>
      <section class="stanza">
        <h2>God is Omniscient</h2>
        <p>All spirituality, all science,<br>All seeing, all perceiving,<br>All knowledge, all wisdom.</p>
      </section>
      <section class="stanza">
        <h2>God is Omnibenevolent</h2>
        <p>All love, all beauty,<br>All truth, all bliss,<br>All merciful, all forgiving,<br>All compassionate.</p>
      </section>
      <section class="stanza">
        <h2>God is Omniconsciousness</h2>
        <p>All universes, all energy fields,<br>All life, all souls,<br>Yet imageless, genderless,<br>Timeless, spaceless, dimensionless,<br>Unending, ever expanding,<br>Unknowable, indescribable,<br>Never born, never dies,<br>Eternal and Immortal,</p>
      </section>
    </div>

    <div class="petals" role="img" aria-label="Row of seven burgundy red petals along the bottom"></div>
    <p class="book-line">The Book Of ONE-LUMEN ARA</p>
  </div>
</div>
</body>
</html>
```